Startup Consultancy - Brochure Design

This needs to be a digital and potential hardcopy of a glossy brochure, designed to really catch the eye of prospective clients and draw them in. I am looking for something alternative from the "usual", but equally in keeping with the IT industry that the business operate in. The business specifically focuses on Print & Document Software and Technology solutions, and this should be considered in the design.

Target Market(s)

SMB and Corporate End Users, + Technology Resellers

Industry/Entity Type

Information Technology

Other font styles liked:
• Avenir

Colors
9d9d9d
848484
c3c3c3
e8e8e8
ffffff
eaeaea
0255a3
3176b5
85acd3

Requirements
Must have
• Company logo displayed on the front, plus any other relevant placements in pages
• Must follow the colour/style in some way of the website (www.brantwellconsultancy.co.uk)
Nice to have
• Some kind of infographical style in the brochure would be good, perhaps around the service listings

```html
<!DOCTYPE html>
<html lang="en">
<head>
<meta charset="utf-8">
<title>Consultancy Brochure – Inside Spread</title>
<link href="https://fonts.googleapis.com/css2?family=Nunito+Sans:wght@400;600&display=swap" rel="stylesheet">
<style>
  :root {
    --blue-deep: #0255a3;
    --blue-mid: #3176b5;
    --blue-soft: #85acd3;
    --grey-dark: #848484;
    --grey-mid: #9d9d9d;
    --grey-light: #c3c3c3;
    --paper: #eef1f3;
    --paper-alt: #e8ecee;
    --text: #5e6266;
    --heading-grey: #4a4f55;
    --teal: #2a9d8f;
  }
  * { margin: 0; padding: 0; box-sizing: border-box; }
  html, body { width: 1200px; height: 906px; overflow: hidden; background: #ffffff; }
  body { font-family: "Nunito Sans", "Avenir", sans-serif; color: var(--text); }
  .spread { display: flex; width: 1200px; height: 906px; }
  .panel {
    position: relative; width: 400px; height: 906px;
    background: linear-gradient(180deg, #f3f5f6 0%, var(--paper) 60%, var(--paper-alt) 100%);
  }
  .panel--why { background: linear-gradient(180deg, #e4e9ec 0%, #dfe5e8 100%); box-shadow: inset -8px 0 14px -10px rgba(0,0,0,.18); }
  .panel--about { box-shadow: inset 8px 0 14px -10px rgba(0,0,0,.12); }
  .panel-title {
    position: absolute; top: 40px; left: 0; width: 100%;
    text-align: center; font-size: 27px; font-weight: 400; letter-spacing: .5px;
    color: var(--heading-grey);
  }
  .panel-title .accent { color: var(--blue-deep); }
  .panel--about .panel-title { color: var(--blue-deep); }
  .lead { position: absolute; font-size: 14px; font-weight: 600; color: var(--blue-deep); }
  .body-text { font-size: 12.5px; line-height: 15.5px; text-align: justify; hyphens: auto; }

  /* Why choose us */
  .panel--why .lead { top: 108px; left: 31px; }
  .reasons { list-style: none; }
  .reason { position: absolute; left: 49px; width: 318px; }
  .reason svg { position: absolute; left: -31px; top: 0; width: 22px; height: 18px; }
  .reason:nth-child(1) { top: 153px; }
  .reason:nth-child(2) { top: 216px; }
  .reason:nth-child(3) { top: 331px; }
  .reason:nth-child(4) { top: 447px; }

  /* Services */
  .service { position: absolute; left: 8px; width: 384px; text-align: center; }
  .service h3 { font-size: 17px; font-weight: 400; color: var(--blue-deep); margin-bottom: 10px; }
  .service p { font-size: 12.5px; line-height: 15.5px; }
  .service--strategy { top: 118px; }
  .service--operational { top: 264px; }
  .service--training { top: 398px; }
  .service--tender { top: 528px; }
  .service-icons { position: absolute; top: 712px; left: 0; width: 100%; display: flex; justify-content: center; gap: 34px; }
  .service-icons svg { width: 48px; height: 46px; }

  /* About */
  .panel--about .lead { top: 112px; left: 25px; }
  .about-copy { position: absolute; top: 144px; left: 25px; width: 342px; }
  .about-copy p { margin-bottom: 15px; }

  .mosaic { position: absolute; left: 0; bottom: 0; width: 400px; }
</style>
</head>
<body>
<main class="spread">

  <section class="panel panel--why">
    <h2 class="panel-title">WHY <span class="accent">CHOOSE</span> US</h2>
    <p class="lead">An alternative and innovative approach</p>
    <ul class="reasons">
      <li class="reason body-text"><svg viewBox="0 0 22 18"><path d="M2 9 L8 15 L20 2" fill="none" stroke="#1d2b45" stroke-width="2.2"/></svg>We take pride, satisfaction and enjoyment from providing clients with clear, non-bias advice.</li>
      <li class="reason body-text"><svg viewBox="0 0 22 18"><path d="M2 9 L8 15 L20 2" fill="none" stroke="#1d2b45" stroke-width="2.2"/></svg>We consistently monitor the marketplace and industry, ensure we are up to speed on trends and technology as well as research and understanding, to deliver professional, experienced and justifiable advice and planning.</li>
      <li class="reason body-text"><svg viewBox="0 0 22 18"><path d="M2 9 L8 15 L20 2" fill="none" stroke="#1d2b45" stroke-width="2.2"/></svg>We maintain memberships with key industry analysts such as Mertvale Research, Halloway Insight and more, along with having representation on European Advisory boards with a view to positively contributing to the imaging and printing industry standards.</li>
      <li class="reason body-text"><svg viewBox="0 0 22 18"><path d="M2 9 L8 15 L20 2" fill="none" stroke="#1d2b45" stroke-width="2.2"/></svg>It is our aim to be the most trusted consultancy in our industry, but to do this we have to earn it.</li>
    </ul>
    <svg class="mosaic" viewBox="0 0 400 320" height="320" role="img" aria-label="Blue and grey geometric triangle mosaic">
      <defs>
        <linearGradient id="mosaicWhy" x1="0" y1="0" x2="1" y2="1">
          <stop offset="0" stop-color="#a9bfd2"/><stop offset=".5" stop-color="#3176b5"/><stop offset="1" stop-color="#9d9d9d"/>
        </linearGradient>
      </defs>
      <polygon points="0,0 180,70 400,150 400,320 0,320" fill="url(#mosaicWhy)"/>
    </svg>
  </section>

  <section class="panel panel--services">
    <h2 class="panel-title">OUR <span class="accent">SERVICES</span></h2>
    <article class="service service--strategy">
      <h3>Strategy Design Services</h3>
      <p>Strategic design and creation for startup Channel Partners or startup divisions within established resellers trying to embed themselves in the Print &amp; Document Solutions market, with hardware, software, services or any combination of those. Let us work with you to create something sustainable and profitable.</p>
    </article>
    <article class="service service--operational">
      <h3>Operational Design Services</h3>
      <p>Print &amp; Document solutions – commercial &amp; administration structure services including greenfield designs and/or improvements on existing structures for Channel Partners to create or improve efficiencies in back office processes.</p>
    </article>
    <article class="service service--training">
      <h3>Training Services</h3>
      <p>We provide training based around Print &amp; Document solution strategy and methodology. The do’s and don’t’s, the changing faces of the market and customer expectations and how the right approach can bring benefits.</p>
    </article>
    <article class="service service--tender">
      <h3>Tender Consultancy &amp; Writing Services</h3>
      <p>We provide tender writing services for all types of End Users who are either unsure of how to structure a tender based around Print &amp; Document solutions or who simply do not have the resource available to do so. As with all of our work, this does involve a co-operative approach to ensure your business needs are met within any tender documentation.</p>
    </article>
    <div class="service-icons">
      <svg viewBox="0 0 48 46" aria-label="Strategy"><g fill="none" stroke="var(--teal)" stroke-width="2"><rect x="10" y="4" width="28" height="38"/><rect x="16" y="24" width="4" height="12"/><rect x="23" y="18" width="4" height="18"/><rect x="30" y="12" width="4" height="24"/></g></svg>
      <svg viewBox="0 0 48 46" aria-label="Operations"><g fill="none" stroke="var(--teal)" stroke-width="2"><path d="M6 30 L24 40 L42 30 L24 20 Z"/><path d="M6 22 L24 32 L42 22 L24 12 Z"/><path d="M6 14 L24 24 L42 14 L24 4 Z"/></g></svg>
      <svg viewBox="0 0 48 46" aria-label="Training"><g fill="none" stroke="#2b2f33" stroke-width="2"><path d="M10 36 L14 24 L32 4 L38 10 L20 30 Z"/><path d="M8 42 H46"/></g></svg>
      <svg viewBox="0 0 48 46" aria-label="Tender"><g stroke="var(--teal)" stroke-width="2" fill="#fff"><path d="M18 14 a14 11 0 1 1 8 22 l-6 6 1-8 a14 11 0 0 1 -3 -20z"/></g><g stroke="#2b2f33" stroke-width="2" fill="#fff"><path d="M18 4 a16 12 0 1 1 -8 22 l-6 6 2-9 a16 12 0 0 1 12 -19z"/></g><g fill="#2b2f33"><circle cx="12" cy="16" r="1.6"/><circle cx="18" cy="16" r="1.6"/><circle cx="24" cy="16" r="1.6"/></g></svg>
    </div>
    <svg class="mosaic" viewBox="0 0 400 110" height="110" role="img" aria-label="Blue and grey geometric triangle mosaic forming a downward chevron">
      <defs>
        <linearGradient id="mosaicServices" x1="0" y1="0" x2="1" y2="0">
          <stop offset="0" stop-color="#3176b5"/><stop offset=".5" stop-color="#9db4c6"/><stop offset="1" stop-color="#0255a3"/>
        </linearGradient>
      </defs>
      <polygon points="0,0 200,100 400,0 400,110 0,110" fill="url(#mosaicServices)"/>
    </svg>
  </section>

  <section class="panel panel--about">
    <h2 class="panel-title">ABOUT US</h2>
    <p class="lead">Taking a different path</p>
    <div class="about-copy body-text">
      <p>We provide services to End User organisations of various sizes, shapes and styles, ranging from SMB through to Enterprise business and even Government, across a range of vertical markets, helping to create forward thinking, future proofed strategic design for Print &amp; Document Workflow solutions - critically however as an entirely independent approach, without any affiliations to manufacturers, software houses or resellers.</p>
      <p>Our expertise, experience and services also support Channel Partners, OEM’s and Distributors, providing guidance and design services for Print &amp; Document Workflow strategies, promoting a customer led focus, efficiency and our own core values of honesty and reliability.</p>
      <p>As a group of very experienced, highly skilled and senior members of the IT/Print/Document Solutions industry, we grew tired of the lack of true, un-biased and trusted advice and support within the industry that both Channel Partners and End Users alike would often receive.</p>
      <p>We don’t sell hardware. We don’t even sell software.</p>
      <p>We remain independent of any manufacturers and are not affiliated to any partner or dealer. What we do provide however is trusted, valuable consultancy, design and advice.</p>
    </div>
    <svg class="mosaic" viewBox="0 0 400 320" height="320" role="img" aria-label="Blue and grey geometric triangle mosaic">
      <defs>
        <linearGradient id="mosaicAbout" x1="0" y1="1" x2="1" y2="0">
          <stop offset="0" stop-color="#3176b5"/><stop offset=".5" stop-color="#85acd3"/><stop offset="1" stop-color="#c3c3c3"/>
        </linearGradient>
      </defs>
      <polygon points="0,205 220,110 400,0 400,320 0,320" fill="url(#mosaicAbout)"/>
    </svg>
  </section>

</main>
</body>
</html>
```